Harvest Lantern Ministry Conference

I am in need of promotional graphics for our upcoming event. This event, titled "Harbor Crest Youth Conference", is a weekend event for teenagers 11-19 years old. They hear from religious speakers, listen to a band, and do other fun activities. Graphic design should be geared to young adults/older teens. Alcohol, drugs, smoking are not permitted. Open to any color combinations you think fit with your design.
Event Info:
November 1-3, 2024
Tellwood Exhibit Hall, Maple Ridge, OR
Speakers: Marcus Linden (man in light blue shirt in attached photo), Tessa Vandermeer (woman in attached photo), Colin Hardy ( man in dark colored shirt in attached photo)
Worship: KW Collective
HarborCrestGather.com
#742GR
Our Organization Logo (attached): Lumenward
Once designed, I need the following graphics file sizes:
-11x17 Vertical Poster design: include all event info AND a "blank" space on the bottom or box for groups to add their own details/information. Also include the QRV logo and our organization logo Lumenward in some way.
-Make an additional copy of the 11x17 pdf with cut and bleed lines for printing, please.
-4x3 horizontal postcard: include all event info on 1 side including Lumenward logo and QRV; blank backside
-Main Graphic Slide: formatted to fit a widescreen 16x9 screen. Include event name, hashtag, QRV and Lumenward logo
-social media graphic(s) for event: can incorporate some or all of the event details. WILLING TO ADJUST BUDGET FOR SOCIAL MEDIA graphics.
-4.25in x 2.75in vertical badge: include event title on front with Lumenward logo
Target Market
ages 11-19
Target Market(s)
11-19 years old
Industry/Entity Type
Christian Youth Ministry

```html
<!DOCTYPE html>
<html lang="en">
<head>
<meta charset="utf-8">
<title>Harbor Crest Youth Conference – Poster</title>
<link rel="stylesheet" href="https://fonts.googleapis.com/css2?family=Poppins:wght@400;500;600;700;800;900&family=Oswald:wght@500;600;700&family=Barlow+Semi+Condensed:wght@700;800&display=swap">
<style>
  :root {
    --navy-deep: #06093f;
    --navy: #0c1690;
    --royal: #1a2cc4;
    --cyan: #27c3ef;
    --cyan-bright: #5ff2f7;
    --violet: #7a48e0;
    --white: #ffffff;
    --pill-dark: #2a3396;
    --photo-dark: #141c5e;
  }
  * { margin: 0; padding: 0; box-sizing: border-box; }
  html, body { width: 866px; height: 1200px; overflow: hidden; background: var(--white); }
  .poster {
    position: relative; width: 866px; height: 1200px;
    font-family: "Poppins", sans-serif; color: var(--white);
  }
  .poster__artwork {
    position: absolute; left: 0; top: 0; width: 866px; height: 1045px; overflow: hidden;
    background:
      radial-gradient(ellipse 60% 45% at 50% 42%, var(--royal) 0%, rgba(26,44,196,0) 70%),
      linear-gradient(180deg, #080c58 0%, var(--navy) 40%, #0a117a 70%, var(--navy-deep) 100%);
  }
  .poster__notes { position: absolute; left: 0; top: 1045px; width: 866px; height: 155px; background: var(--white); }

  .title { position: absolute; left: 0; width: 100%; text-align: center; display: block; }
  .title__lead { top: 56px; font-weight: 800; font-size: 64px; letter-spacing: -1px; line-height: 1; }
  .title__main {
    top: 118px; font-weight: 900; font-size: 168px; line-height: 1;
    letter-spacing: -3px;
    background: linear-gradient(180deg, #e9fffe 0%, var(--cyan-bright) 45%, #1ac9e0 100%);
    -webkit-background-clip: text; background-clip: text; color: transparent;
    filter: drop-shadow(4px 3px 0 var(--violet));
  }
  .title__sub { top: 270px; font-weight: 600; font-size: 42px; letter-spacing: 22px; padding-left: 22px; line-height: 1; }

  .speakers-frame {
    position: absolute; left: 44px; top: 362px; width: 778px; height: 327px;
    border: 2px solid var(--white);
  }
  .speakers-frame__label {
    position: absolute; left: 50%; top: -13px; transform: translateX(-50%);
    padding: 0 8px; background: #0e1a9c; color: var(--cyan-bright);
    font-weight: 500; font-size: 19px; letter-spacing: 6px; white-space: nowrap; line-height: 24px;
  }
  .speaker-photo { position: absolute; }
  .speaker-photo--left {
    left: 70px; top: 400px; width: 265px; height: 380px;
    background: linear-gradient(180deg, rgba(201,207,230,0.9) 0%, rgba(150,160,210,0.75) 55%, rgba(12,22,144,0) 100%);
    border-radius: 120px 120px 0 0;
  }
  .speaker-photo--center {
    left: 320px; top: 385px; width: 280px; height: 420px;
    background: linear-gradient(180deg, rgba(75,90,168,0.85) 0%, var(--photo-dark) 45%, rgba(6,9,63,0) 100%);
    border-radius: 130px 130px 0 0;
  }
  .speaker-photo--right {
    left: 540px; top: 395px; width: 296px; height: 500px;
    background: linear-gradient(180deg, rgba(120,150,205,0.8) 0%, rgba(110,140,200,0.6) 50%, rgba(12,22,144,0) 100%);
    border-radius: 130px 130px 0 0;
  }
  .speaker-name {
    position: absolute; top: 648px; width: 240px; text-align: center;
    font-family: "Barlow Semi Condensed", sans-serif; font-weight: 800; font-size: 33px;
    line-height: 34px; text-transform: uppercase;
    text-shadow: 0 2px 8px rgba(6,9,63,0.6);
  }
  .speaker-name--left { left: 76px; }
  .speaker-name--center { left: 348px; }
  .speaker-name--right { left: 595px; }

  .event-date { position: absolute; left: 0; top: 740px; width: 100%; height: 110px; }
  .event-date__day {
    position: absolute; top: 0; font-family: "Oswald", sans-serif; font-weight: 700;
    font-size: 128px; line-height: 110px;
  }
  .event-date__day--start { left: 234px; }
  .event-date__day--end { left: 404px; }
  .event-date__to {
    position: absolute; left: 302px; top: 14px; width: 84px; height: 84px;
    border-radius: 50%; background: var(--cyan); color: var(--navy-deep);
    font-family: "Oswald", sans-serif; font-weight: 600; font-size: 44px; line-height: 84px; text-align: center;
  }
  .event-date__month {
    position: absolute; left: 487px; top: 10px; color: var(--cyan);
    font-weight: 800; font-size: 62px; line-height: 56px; letter-spacing: -1px;
  }
  .event-date__year {
    position: absolute; left: 487px; top: 66px; font-weight: 500; font-size: 32px;
    letter-spacing: 12px; line-height: 32px;
  }

  .venue {
    position: absolute; left: 0; top: 873px; width: 100%; text-align: center;
    font-size: 27px; font-weight: 400; line-height: 36px;
  }
  .venue__pin { display: inline-block; width: 22px; height: 26px; vertical-align: -3px; margin-right: 8px; }

  .worship {
    position: absolute; left: 222px; top: 908px; width: 420px; height: 38px; display: flex;
    border-radius: 10px; overflow: hidden; box-shadow: -3px 3px 0 rgba(6,9,63,0.8);
    font-size: 25px; line-height: 38px; background: var(--pill-dark);
  }
  .worship__label { background: var(--cyan); color: var(--navy-deep); padding: 0 8px 0 16px; border-radius: 10px; }
  .worship__name { flex: 1; padding: 0 12px; text-align: center; }

  .org-mark { position: absolute; display: flex; align-items: center; gap: 8px; font-weight: 700; color: var(--white); line-height: 1; }
  .org-mark--partner { left: 70px; top: 966px; font-size: 34px; }
  .org-mark--host { left: 690px; top: 970px; font-size: 24px; }
  .org-mark__dot { width: 26px; height: 26px; border-radius: 50%; background: var(--cyan); }

  .site-url {
    position: absolute; left: 0; top: 960px; width: 100%; text-align: center;
    font-size: 27px; letter-spacing: 3.5px; line-height: 34px;
  }
  .hashtag {
    position: absolute; left: 50%; top: 1000px; transform: translateX(-50%);
    background: var(--cyan); color: var(--navy-deep); border-radius: 7px;
    font-weight: 700; font-size: 19px; line-height: 27px; padding: 0 8px;
  }
</style>
</head>
<body>
<main class="poster">
  <section class="poster__artwork">
    <h1>
      <span class="title title__lead">HARBOR CREST</span>
      <span class="title title__main">YOUTH</span>
      <span class="title title__sub">CONFERENCE</span>
    </h1>

    <div class="speaker-photo speaker-photo--left" role="img" aria-label="Portrait photo of speaker Tessa Vandermeer"></div>
    <div class="speaker-photo speaker-photo--center" role="img" aria-label="Portrait photo of speaker Marcus Linden"></div>
    <div class="speaker-photo speaker-photo--right" role="img" aria-label="Photo of speaker Colin Hardy speaking into a microphone"></div>

    <div class="speakers-frame">
      <span class="speakers-frame__label">OUR SPEAKERS</span>
    </div>

    <p class="speaker-name speaker-name--left">Tessa<br>Vandermeer</p>
    <p class="speaker-name speaker-name--center">Marcus<br>Linden</p>
    <p class="speaker-name speaker-name--right">Colin<br>Hardy</p>

    <div class="event-date">
      <span class="event-date__day event-date__day--start">1</span>
      <span class="event-date__to">TO</span>
      <span class="event-date__day event-date__day--end">3</span>
      <span class="event-date__month">NOV</span>
      <span class="event-date__year">2024</span>
    </div>

    <p class="venue">
      <svg class="venue__pin" viewBox="0 0 22 26" aria-hidden="true">
        <path d="M11 2a7 7 0 0 0-7 7c0 5 7 12 7 12s7-7 7-12a7 7 0 0 0-7-7z" fill="none" stroke="#fff" stroke-width="2"/>
        <circle cx="11" cy="9" r="2.5" fill="none" stroke="#fff" stroke-width="2"/>
        <path d="M5 19c-3 1-3 4 6 4s9-3 6-4" fill="none" stroke="#fff" stroke-width="1.8"/>
      </svg>Tellwood Exhibit Hall, Maple Ridge, OR
    </p>

    <div class="worship">
      <span class="worship__label">WORSHIP:</span>
      <span class="worship__name">KW COLLECTIVE</span>
    </div>

    <div class="org-mark org-mark--partner"><span class="org-mark__dot"></span>QRV</div>
    <p class="site-url">HarborCrestGather.com</p>
    <span class="hashtag">#742GR</span>
    <div class="org-mark org-mark--host">Lumenward</div>
  </section>
  <section class="poster__notes" aria-label="Space for group details"></section>
</main>
</body>
</html>
```